Brindlewood Business Card Design

Small Company
looking to ramp up work need business cards sick of everyone asking for a card
client base is broad.
keep it simple
Just want on the reverse of the card somewhere for me to write details for clients
appointments etc..
want to use the phrase
"Your safe, reliable and trust worthy Tradesmen"

Industry/Entity Type

Business

Contact Information for Business Card

Brindlewood Electrical Solutions Pty Ltd
Director Gregory Brindlewood
email - brindlewoodelectricalsolutions@zentromail.net
Ph - 03 95418276
Mobile - 0417592836
Domestic, Industrial, Commercial & Mining
Electrical, Solar, Communications & Fibre
REC: 41873

```html
<!DOCTYPE html>
<html lang="en">
<head>
<meta charset="utf-8">
<title>Brindlewood Electrical Solutions – Business Card</title>
<link href="https://fonts.googleapis.com/css2?family=Noto+Sans:wght@400;700&family=PT+Sans:wght@400&display=swap" rel="stylesheet">
<style>
  :root {
    --page: #e9e9eb;
    --card: #ffffff;
    --navy: #1f2a6b;
    --brand-blue: #3a4fb0;
    --band: #3d52b4;
    --grey-text: #6d6d6d;
    --ink: #333333;
    --rule: #3d52b4;
  }
  * { box-sizing: border-box; margin: 0; padding: 0; }
  html, body {
    width: 1200px; height: 1000px; overflow: hidden;
    background: var(--page);
    font-family: "Noto Sans", Arial, sans-serif;
  }
  .sheet {
    width: 1200px; height: 1000px;
    display: flex; flex-direction: column; align-items: center; justify-content: center;
    gap: 40px;
  }
  .card {
    position: relative;
    width: 740px; height: 450px;
    background: var(--card);
    box-shadow: 0 6px 22px rgba(0,0,0,0.18);
    overflow: hidden;
  }

  /* Wordmark: one colour, one weight */
  .brand {
    position: absolute;
    font-family: "PT Sans", Arial, sans-serif;
    font-weight: 400; color: var(--brand-blue);
    line-height: 1; white-space: nowrap;
  }
  .brand__name { display: block; }
  .brand__sub { display: block; letter-spacing: 0.5px; margin-top: 4px; }

  /* Front */
  .front__panel {
    position: absolute; left: 40px; top: 40px; width: 400px; height: 300px;
    background: linear-gradient(180deg, #ffffff 0%, #f6f6f7 100%);
    box-shadow: 6px 6px 14px rgba(0,0,0,0.10);
  }
  .front__brand { left: 95px; top: 95px; }
  .front__brand .brand__name { font-size: 52px; }
  .front__brand .brand__sub { font-size: 20px; }
  .front__services {
    position: absolute; left: 70px; top: 225px; width: 340px;
    text-align: center; font-size: 13px; line-height: 1.45; color: var(--ink);
  }
  .front__person { position: absolute; left: 478px; top: 112px; }
  .front__name {
    font-size: 21px; font-weight: 700; color: var(--navy); letter-spacing: 0.3px;
    white-space: nowrap;
  }
  .front__role { font-size: 15px; color: var(--grey-text); margin-top: 2px; }
  .contact-band {
    position: absolute; left: 40px; right: 40px; bottom: 40px; height: 68px;
    background: var(--band); color: #fff;
    display: grid; grid-template-rows: 1fr 1fr; padding: 6px 18px;
    font-size: 15px;
  }
  .contact-band__row { display: flex; align-items: center; gap: 8px; white-space: nowrap; }
  .contact-band__row--split { justify-content: flex-end; gap: 60px; }
  .contact-item { display: flex; align-items: center; gap: 8px; }
  .contact-item svg { width: 14px; height: 14px; fill: #fff; }

  /* Back */
  .back__label {
    position: absolute; left: 60px; top: 52px;
    font-size: 14px; color: var(--grey-text);
  }
  .back__brand { left: 60px; bottom: 52px; }
  .back__brand .brand__name { font-size: 36px; }
  .back__brand .brand__sub { font-size: 14px; }
  .back__rule {
    position: absolute; left: 290px; right: 60px; bottom: 108px;
    border-top: 1.5px solid var(--rule);
  }
  .back__tagline {
    position: absolute; right: 60px; bottom: 80px;
    font-size: 16px; color: var(--brand-blue); white-space: nowrap;
  }
</style>
</head>
<body>
<main class="sheet">

  <section class="card card--front" aria-label="Business card front">
    <div class="front__panel"></div>
    <div class="brand front__brand">
      <span class="brand__name">Brindlewood</span>
      <span class="brand__sub">Electrical Solutions</span>
    </div>
    <p class="front__services">"Domestic, Industrial, Commercial &amp; Mining Electrical,<br>Solar, Communications &amp; Fibre "<br>REC: 41873</p>
    <div class="front__person">
      <p class="front__name">Gregory Brindlewood</p>
      <p class="front__role">Director</p>
    </div>
    <div class="contact-band">
      <div class="contact-band__row">
        <span>@ :</span><span>brindlewoodelectricalsolutions@zentromail.net</span>
      </div>
      <div class="contact-band__row contact-band__row--split">
        <span class="contact-item">
          <svg viewBox="0 0 24 24" aria-hidden="true"><path d="M6.6 10.8a15.1 15.1 0 0 0 6.6 6.6l2.2-2.2a1 1 0 0 1 1-.25 11.4 11.4 0 0 0 3.6.57 1 1 0 0 1 1 1V20a1 1 0 0 1-1 1A17 17 0 0 1 3 4a1 1 0 0 1 1-1h3.5a1 1 0 0 1 1 1c0 1.25.2 2.45.57 3.570a1 1 0 0 1-.25 1z"/></svg>
          : 03 95418276
        </span>
        <span class="contact-item">
          <svg viewBox="0 0 24 24" aria-hidden="true"><path d="M7 2h10a2 2 0 0 1 2 2v16a2 2 0 0 1-2 2H7a2 2 0 0 1-2-2V4a2 2 0 0 1 2-2zm0 3v12h10V5z"/></svg>
          : 0417592836
        </span>
      </div>
    </div>
  </section>

  <section class="card card--back" aria-label="Business card back">
    <p class="back__label">Appointments details:</p>
    <div class="brand back__brand">
      <span class="brand__name">Brindlewood</span>
      <span class="brand__sub">Electrical Solutions</span>
    </div>
    <div class="back__rule"></div>
    <p class="back__tagline">Your safe, reliable and trust worthy Tradesmen</p>
  </section>

</main>
</body>
</html>
```